Design a Flyer for Sports Concussion Clinic

Need a flyer made for a sports concussion league. This flyer will be handed out to youth athletes in the community. Should be a very clean and very professional design. Any images should be professional looking (clip art of shadows), but should include multiple sports (american football, basketball, soccer, baseball, volleyball).

Size is 8.5 x 5.5 inches. For print media, so should be hi-res.

Content:
------------------------------------------------------------------
Sport Concussion Clinic
o Specifically designed to care for young athletes (10 to 25 year of age) who sustain a concussion during sport
o Goal of the clinic is to evaluate and treat these athletes so they can safely return to sport.
o Clinic held at Harbourview Community Hospital one - two times per week depending on demand
o Physician referral is required and may be obtained from your family or emergency room physician
o Clinic staffed by two Sport Docs - Dr Melissa Thornbury and Dr Peter Hollis, with support from Athletic Therapist Douglas Kinnaird and Physio Therapist Talia Brisco.
o Formal SCAT 3 testing for baseline assessment
o Structured Return to Play (RTP) Protocol

Dr Melissa Thornbury - office number 487-3906, fax 487-3905.

Note: All design materials and source files must be submitted after the project is awarded. You will not be able to copyright or post the project materials in your portfolio.

```html
<!DOCTYPE html>
<html lang="en">
<head>
<meta charset="utf-8">
<title>Sport Concussion Clinic Flyer</title>
<link rel="stylesheet" href="https://fonts.googleapis.com/css2?family=Tinos:wght@700&family=Arimo:ital,wght@0,400;1,700&display=swap">
<style>
  :root {
    --brown-dark: #8a4a16;
    --brown: #b0662a;
    --brown-light: #d4924a;
    --gold-deep: #e3a933;
    --gold: #f2cd63;
    --cream: #fdf3cf;
    --box-fill: #fdf6dc;
    --box-border: #d9ac5c;
    --ink: #2b1b0c;
    --white: #ffffff;
    --silhouette: #1e1209;
  }
  html, body { margin: 0; padding: 0; overflow: hidden; background: var(--white); }
  .flyer {
    position: relative;
    width: 1200px;
    height: 776px;
    overflow: hidden;
    background: radial-gradient(ellipse at 50% 45%, var(--cream) 0%, var(--gold) 60%, var(--gold-deep) 100%);
    font-family: "Arimo", Arial, sans-serif;
    color: var(--ink);
  }
  .backdrop { position: absolute; inset: 0; }
  .title {
    position: absolute;
    left: 78px;
    top: 18px;
    margin: 0;
    font-family: "Tinos", "Times New Roman", serif;
    font-weight: 700;
    font-size: 46px;
    line-height: 47px;
    letter-spacing: 1px;
    color: var(--white);
    text-shadow: -2px -2px 0 #3b1d06, 2px -2px 0 #3b1d06, -2px 2px 0 #3b1d06, 2px 2px 0 #3b1d06, 3px 3px 4px rgba(0,0,0,.5);
  }
  .tagline {
    position: absolute;
    right: 42px;
    top: 28px;
    margin: 0;
    font-style: italic;
    font-weight: 700;
    font-size: 20px;
    color: var(--white);
    text-shadow: 1px 1px 2px rgba(60,25,0,.6);
  }
  .athlete {
    position: absolute;
    background: linear-gradient(180deg, var(--silhouette), #3a2210);
    border-radius: 40px 40px 14px 14px;
  }
  .facts {
    position: absolute;
    left: 113px;
    top: 217px;
    width: 1004px;
    margin: 0;
    padding: 0;
    list-style: none;
  }
  .fact {
    box-sizing: border-box;
    margin-bottom: 10px;
    padding: 5px 13px 5px 13px;
    background: var(--box-fill);
    border: 2px solid var(--box-border);
    border-radius: 6px;
    box-shadow: 0 1px 3px rgba(120,70,10,.25);
    font-size: 21px;
    line-height: 28px;
    text-align: justify;
  }
  .contact {
    position: absolute;
    left: 684px;
    top: 693px;
    font-family: "Tinos", "Times New Roman", serif;
    font-weight: 700;
    color: var(--ink);
  }
  .contact-name { margin: 0; font-size: 23px; line-height: 26px; }
  .contact-line { margin: 0; font-size: 20px; line-height: 26px; }
</style>
</head>
<body>
<main class="flyer">
  <svg class="backdrop" width="1200" height="776" viewBox="0 0 1200 776" aria-hidden="true">
    <defs>
      <linearGradient id="bandTop" x1="0" y1="0" x2="1" y2="0">
        <stop offset="0" stop-color="#7c3f10"/>
        <stop offset="0.5" stop-color="#b36a2c"/>
        <stop offset="1" stop-color="#9a5420"/>
      </linearGradient>
      <linearGradient id="bandBottom" x1="0" y1="0" x2="1" y2="0">
        <stop offset="0" stop-color="#d08a3c"/>
        <stop offset="0.6" stop-color="#a85d22"/>
        <stop offset="1" stop-color="#8a4814"/>
      </linearGradient>
    </defs>
    <path d="M0 0 H1200 V95 C1000 100 820 120 620 130 C420 140 250 160 0 185 Z" fill="url(#bandTop)"/>
    <path d="M0 185 C250 160 420 140 620 130 C820 120 1000 100 1200 95 V108 C1000 115 800 140 600 150 C400 160 220 180 0 200 Z" fill="#fff4cf" opacity=".85"/>
    <path d="M0 776 V700 C260 690 420 650 640 650 C860 650 1000 690 1200 680 V776 Z" fill="#fbedc0"/>
    <path d="M0 700 C260 690 420 650 640 650 C860 650 1000 690 1200 680 V668 C1000 672 860 635 640 636 C420 637 260 675 0 690 Z" fill="url(#bandBottom)"/>
  </svg>

  <h1 class="title">SPORT<br>CONCUSSION<br>CLINIC</h1>
  <p class="tagline">Specifically designed to care for young athletes</p>

  <div class="athlete" role="img" aria-label="Silhouette of a volleyball player bumping a ball" style="left:280px;top:125px;width:110px;height:80px;"></div>
  <div class="athlete" role="img" aria-label="Silhouette of a basketball player shooting" style="left:482px;top:33px;width:56px;height:176px;"></div>
  <div class="athlete" role="img" aria-label="Silhouette of a soccer player dribbling a ball" style="left:632px;top:76px;width:90px;height:134px;"></div>
  <div class="athlete" role="img" aria-label="Silhouette of an American football player running with the ball" style="left:826px;top:50px;width:70px;height:160px;"></div>
  <div class="athlete" role="img" aria-label="Silhouette of a baseball batter swinging" style="left:980px;top:58px;width:128px;height:152px;"></div>

  <ul class="facts">
    <li class="fact">Specifically designed to care for young athletes (10 to 25 year of age) who sustain a concussion during sport.</li>
    <li class="fact">Goal of the clinic is to evaluate and treat these athletes so they can safely return to sport.</li>
    <li class="fact">Clinic held at Harbourview Community Hospital one - two times per week depending on demand.</li>
    <li class="fact">Physician referral is required and may be obtained from your family or emergency room physician.</li>
    <li class="fact">Clinic staffed by two Sport Docs - Dr Melissa Thornbury and Dr Peter Hollis, with support from Athletic Therapist Douglas Kinnaird and Physio Therapist Talia Brisco.</li>
    <li class="fact">Formal SCAT 3 testing for baseline assessment.</li>
    <li class="fact">Structured Return to Play (RTP) Protocol.</li>
  </ul>

  <address class="contact">
    <p class="contact-name">Dr. Melissa Thornbury.</p>
    <p class="contact-line">Office number 487-3906, fax 487-3905.</p>
  </address>
</main>
</body>
</html>
```